Pack Design for High Quality Marine Collagen Powder

We're looking for a quality full pack design (front and back) to sell on Brixora. We need a 2D version of front and back image in photoshop and JPG. We also need a 3D version of front and back for marketing purposes.

As many colour as needed, printing is CMYK + White digital printed.

Front of pack:

Text as follows:

Headline: 'Wild Marine Hydrolysed Collagen Powder' ...(The emphasis needs to be on the word Collagen)

Text: Essential Protein For Muscle, Hair and Skin | Rich in Amino Acids | Certified KVM Sustainably Sourced | Yeast & Gluten Free | No Additives | Unflavoured and Odorless | Water-Soluble

200g

(KVM and Sustainable logos)

Plavendors logo at the bottom of pack. Doesn't need to be too prominent.

Back of pack:

Ingredients:
100% Pure Hydrolysed Marine Collagen (Natural)
Derived from Fish

Nutritional Information: (Please put this into a table)
Typical Values Per 10g Serving
Energy 159Kj/38kCal
Protein 9.5g
Carbohydrates 0.02g
Of which sugars 0.02g
Fat 0g
Fibre 0g
Sodium 0g
Free from GMO, Fat, Carbohydrates, Purine, Preservatives, Artificial colours/flavours
Amino Acids 99.9%
Of which essential 14.5%

This supplement should not be used as a substitute for a varied diet Do not exceed the recommended daily dose.

Please consult a healthcare practitioner if you are pregnant or taking prescription medicine before using this product.

Recommended daily dose

10-15g daily

Directions for use
Add 10g of powder to 250ml of cold water, coffee, smoothie, shake, juice, protein shake, porridge or soups.

To ensure optimum absorption, consume collagen powder at least 30 mins before a meal.

Storage information: Store in a cool dry place away from sunlight, moisture, and heat. Keep out of reach of animals and children. Keep contents dry. Reject if pack seal is broken.

Brixora Barcode image

To reorder, go to www.dunmarrowfield.co.uk

Produced in the UK

More notes:

We have included the protein module design for inspiration of pack design along with some other designs that we like.

Pack dimensions 19cm (height) x 15cm (width). The top 2cm will be torn off by the user, so should not contain any key information.

Target Market(s)

Health conscious adults over 25

Industry/Entity Type

Marine

Colors

Designer to choose colors to be used in the design.

Requirements
Must have
• This product must stand out on Brixora and be seen. But not too busy in design and vivid enough to get clicks.
• Please only submit designs in 3D. We need a tight shadow to the right of the pack
• Final design needs to be high res ready to send to the printers with a normal bleed space around the edge.
Nice to have
• The final design should communicate quality, sustainability. The background should be clear - white ideally. Collagen is a product for health - specifically for skin and bone health.
• To help us choose, we would appreciate if you photoshop your design in 3D into an Brixora listings page - so we can see that it stands out.
Should not have
• Be too busy. Can't be bland. Text must be very readable.

```html
<!DOCTYPE html>
<html lang="en">
<head>
<meta charset="UTF-8">
<title>Wild Marine Hydrolysed Collagen – Pouch Front</title>
<link rel="stylesheet" href="https://fonts.googleapis.com/css2?family=Montserrat:wght@800&family=Roboto:wght@300;400&display=swap">
<style>
  :root {
    --bg: #e6ecee;
    --pouch-light: #f7f7f7;
    --pouch-mid: #ebebeb;
    --pouch-edge: #dcdcdc;
    --seal-line: #d2d2d2;
    --ink-grey: #8a8d90;
    --ink-soft: #9a9da0;
    --teal: #1fb3a5;
    --teal-deep: #1a9cb0;
    --sea-deep: #1b4f8a;
    --sea-blue: #1e8fd0;
    --sea-cyan: #3cc6e0;
    --sea-yellow: #d9dc5a;
    --badge: #1a9a97;
  }
  * { box-sizing: border-box; margin: 0; padding: 0; }
  html, body { width: 1200px; height: 900px; overflow: hidden; }
  body { background: var(--bg); font-family: "Roboto", Arial, sans-serif; }

  .pouch {
    position: absolute;
    left: 310px; top: 25px;
    width: 580px; height: 850px;
    background: linear-gradient(90deg, var(--pouch-edge) 0%, var(--pouch-light) 12%, var(--pouch-light) 80%, var(--pouch-mid) 100%);
    border-radius: 4px 4px 14px 14px;
    overflow: hidden;
  }
  .pouch__seal {
    position: absolute; left: 20px; right: 20px; top: 94px;
    border-top: 2px solid var(--seal-line);
    border-bottom: 1px solid var(--seal-line);
    height: 6px;
  }

  .headline { position: absolute; top: 168px; left: 0; right: 0; text-align: center; }
  .headline__pre {
    font-weight: 400; font-size: 24px; letter-spacing: 2.5px;
    color: var(--ink-grey); text-transform: uppercase;
  }
  .headline__main {
    font-family: "Montserrat", Arial, sans-serif; font-weight: 800;
    font-size: 66px; line-height: 1; margin-top: 4px; letter-spacing: 0.5px;
    background: linear-gradient(90deg, var(--teal), var(--teal-deep));
    -webkit-background-clip: text; background-clip: text; color: transparent;
  }
  .headline__post {
    font-weight: 300; font-size: 31px; letter-spacing: 7px;
    color: var(--ink-grey); text-transform: uppercase; margin-top: 6px;
  }

  .sea-visual {
    position: absolute; left: 20px; right: 20px; top: 325px; height: 250px;
    background:
      linear-gradient(168deg, transparent 30%, var(--sea-yellow) 42%, var(--sea-cyan) 52%, var(--sea-blue) 64%, var(--sea-deep) 78%, transparent 92%);
    -webkit-mask-image: linear-gradient(180deg, transparent 0%, #000 25%, #000 70%, transparent 100%);
    mask-image: linear-gradient(180deg, transparent 0%, #000 25%, #000 70%, transparent 100%);
  }

  .claims {
    position: absolute; top: 620px; left: 0; right: 0;
    text-align: center; font-size: 13px; line-height: 22px; color: var(--ink-soft);
  }
  .claims .sep { color: var(--teal); padding: 0 3px; }

  .brand { position: absolute; left: 112px; top: 724px; }
  .brand__name { font-size: 21px; font-weight: 400; color: #4a4d50; }
  .brand__sub { font-size: 11px; color: #4a4d50; text-align: right; margin-top: -2px; }
  .net-weight {
    position: absolute; left: 188px; top: 770px;
    font-size: 15px; color: var(--teal);
  }

  .cert-badge {
    position: absolute; left: 370px; top: 705px; width: 108px; height: 76px;
    border: 1px solid #cfcfcf; padding: 10px 8px;
  }
  .cert-badge span { display: block; width: 100%; height: 100%; background: var(--badge); border-radius: 2px; }
</style>
</head>
<body>
  <main class="pouch">
    <div class="pouch__seal"></div>

    <header class="headline">
      <p class="headline__pre">Wild Marine Hydrolysed</p>
      <h1 class="headline__main">COLLAGEN</h1>
      <p class="headline__post">Protein Powder</p>
    </header>

    <div class="sea-visual" role="img" aria-label="Flowing ocean wave photograph in blue, cyan and yellow tones"></div>

    <p class="claims">
      Essential Protein For Muscle, Hair and Skin<span class="sep">|</span>Rich in Amino Acids<span class="sep">|</span><br>
      Certified KVM Sustainably Sourced<span class="sep">|</span>Yeast &amp; Gluten Free<span class="sep">|</span>No Additives<span class="sep">|</span><br>
      Unflavoured and Odorless<span class="sep">|</span>Water-Soluble
    </p>

    <div class="brand">
      <p class="brand__name">Plavendors</p>
      <p class="brand__sub">Health Products</p>
    </div>
    <p class="net-weight">200g</p>

    <div class="cert-badge" role="img" aria-label="Sustainability certification badge"><span></span></div>
  </main>
</body>
</html>
```